Create a newspaper layout from word files and photos provided for wedding

For our wedding we want a "newspaper style" memento for guests. It will include articles I have written about me and my fiancee and our family and friends as well as photos and anecdotes.
We require someone to take our words and design content and turn it into a file that we can get printed.
We will provde content - we want your layout skill.

Full file is available at
https://www.filecrate-share.net/sh/q7mtpw284vkbn52/KRTVbmQpLwZxHsYdNfGeUkTrJ?oref=e&n=726153048

Instructions are included.Utilise written content to create wedding newspaper and add photos were possible.
Black and white but photos should be in colour.
Must be 4 or 8 pages.
If text provided is too long notes to be provided to us where cuts are required.

We have committed payment.
We seek designs to review on Sunday evening.
We will select designs at this time or earlier if appropriate design is submitted using full layout.
Once selected we will work with designer to refine and finalise job by Tuesday next week when it must go to printer.

Thanks and if there are an questions post away.
Updates

Target Market(s)

Wedding guests

Industry/Entity Type

Wedding

Font styles to use
Serif

Requirements
Must have
• Style and photographs
Should not have
• Too much blank space
• Too small text

```html
<!DOCTYPE html>
<html lang="en">
<head>
<meta charset="utf-8">
<title>The Bridesmaids &amp; The Best Man</title>
<link rel="stylesheet" href="https://fonts.googleapis.com/css2?family=UnifrakturMaguntia&family=Open+Sans:wght@700;800&family=Tinos&display=swap">
<style>
  :root {
    --paper: #ffffff;
    --ink: #111111;
    --caption: #4a4a4a;
    --flourish: #d9cfc6;
    --photo-warm: #d98a4e;
    --photo-green: #7f9a5a;
    --photo-rose: #c98e8a;
  }
  * { box-sizing: border-box; margin: 0; padding: 0; }
  html, body { width: 848px; height: 1200px; overflow: hidden; background: var(--paper); }
  .page {
    position: relative;
    width: 848px;
    height: 1200px;
    background: var(--paper);
    color: var(--ink);
    font-family: "Tinos", "Times New Roman", serif;
  }
  .masthead-line {
    position: absolute;
    top: 22px;
    font-size: 19px;
    letter-spacing: 0.2px;
  }
  .edition { left: 46px; }
  .issue-date { right: 38px; }

  .section-title {
    position: absolute;
    left: 0;
    width: 848px;
    text-align: center;
    font-family: "UnifrakturMaguntia", "Old English Text MT", serif;
    font-weight: 400;
    font-size: 58px;
    line-height: 1;
  }
  .flourish {
    position: absolute;
    width: 48px;
    height: 96px;
    background: linear-gradient(180deg, var(--flourish), #efe8e2);
    border-radius: 6px;
  }

  .divider { position: absolute; left: 420px; width: 14px; }

  .article {
    position: absolute;
    width: 380px;
    text-align: center;
  }
  .col-left { left: 36px; }
  .col-right { left: 436px; }

  .person-name {
    font-family: "Open Sans", Arial, sans-serif;
    font-weight: 800;
    font-size: 23px;
    line-height: 26px;
    letter-spacing: 0.1px;
  }
  .photo {
    position: relative;
    width: 138px;
    height: 90px;
    margin: 5px auto 0;
    background: linear-gradient(135deg, var(--photo-warm) 0%, var(--photo-rose) 45%, var(--photo-green) 100%);
    opacity: 0.85;
  }
  .photo-label {
    position: absolute;
    left: 0;
    right: 0;
    top: 42px;
    font-size: 18px;
    color: var(--caption);
  }
  .story {
    margin-top: -6px;
    font-size: 15.5px;
    line-height: 20.8px;
  }
  .drop-cap {
    font-family: "UnifrakturMaguntia", "Old English Text MT", serif;
    font-size: 34px;
    line-height: 0;
    vertical-align: -6px;
  }
</style>
</head>
<body>
<div class="page">
  <div class="masthead-line edition">SPECIAL EDITION</div>
  <div class="masthead-line issue-date">Month dd, yyyy</div>

  <!-- Bridesmaids -->
  <div class="flourish" style="left:40px;top:56px;" role="img" aria-label="Decorative corner flourish"></div>
  <div class="flourish" style="right:34px;top:56px;" role="img" aria-label="Decorative corner flourish"></div>
  <h1 class="section-title" style="top:72px;">The Bridesmaids</h1>

  <svg class="divider" style="top:156px;height:450px;" viewBox="0 0 14 450" aria-hidden="true">
    <line x1="7" y1="10" x2="7" y2="440" stroke="#111" stroke-width="1.4"/>
    <path d="M7 0 L11 16 L7 12 L3 16 Z M7 450 L11 434 L7 438 L3 434 Z" fill="#111"/>
    <circle cx="7" cy="120" r="1.6" fill="#111"/>
    <circle cx="7" cy="225" r="1.6" fill="#111"/>
    <circle cx="7" cy="330" r="1.6" fill="#111"/>
  </svg>

  <article class="article col-left" style="top:150px;">
    <h2 class="person-name">BRIDESMAID’S NAME</h2>
    <div class="photo" role="img" aria-label="Bridesmaid photo"><span class="photo-label">Her Photo Here</span></div>
    <p class="story"><span class="drop-cap">Y</span>our story here your story here your story here your story here your story here your story your story here your story here your story here your story here your story here your story here your story here your story here your story here your story here</p>
  </article>
  <article class="article col-right" style="top:147px;">
    <h2 class="person-name">BRIDESMAID’S NAME</h2>
    <div class="photo" role="img" aria-label="Bridesmaid photo"><span class="photo-label">Her Photo Here</span></div>
    <p class="story"><span class="drop-cap">Y</span>our story here your story here your story here your story here your story here your story your story here your story here your story here your story here your story here your story here your story here your story here your story here your story here</p>
  </article>
  <article class="article col-left" style="top:385px;">
    <h2 class="person-name">BRIDESMAID’S NAME</h2>
    <div class="photo" role="img" aria-label="Bridesmaid photo"><span class="photo-label">Her Photo Here</span></div>
    <p class="story"><span class="drop-cap">Y</span>our story here your story here your story here your story here your story here your story your story here your story here your story here your story here your story here your story here your story here your story here your story here your story here</p>
  </article>
  <article class="article col-right" style="top:382px;">
    <h2 class="person-name">BRIDESMAID’S NAME</h2>
    <div class="photo" role="img" aria-label="Bridesmaid photo"><span class="photo-label">Her Photo Here</span></div>
    <p class="story"><span class="drop-cap">Y</span>our story here your story here your story here your story here your story here your story your story here your story here your story here your story here your story here your story here your story here your story here your story here your story here</p>
  </article>

  <!-- Best Man -->
  <div class="flourish" style="left:40px;top:630px;" role="img" aria-label="Decorative corner flourish"></div>
  <div class="flourish" style="right:34px;top:630px;" role="img" aria-label="Decorative corner flourish"></div>
  <h1 class="section-title" style="top:645px;">The Best Man</h1>

  <svg class="divider" style="top:728px;height:452px;" viewBox="0 0 14 452" aria-hidden="true">
    <line x1="7" y1="10" x2="7" y2="442" stroke="#111" stroke-width="1.4"/>
    <path d="M7 0 L11 16 L7 12 L3 16 Z M7 452 L11 436 L7 440 L3 436 Z" fill="#111"/>
    <circle cx="7" cy="120" r="1.6" fill="#111"/>
    <circle cx="7" cy="226" r="1.6" fill="#111"/>
    <circle cx="7" cy="332" r="1.6" fill="#111"/>
  </svg>

  <article class="article col-left" style="top:721px;">
    <h2 class="person-name">BEST MAN’S NAME</h2>
    <div class="photo" role="img" aria-label="Best man photo"><span class="photo-label">His Photo Here</span></div>
    <p class="story"><span class="drop-cap">Y</span>our story here your story here your story here your story here your story here your story your story here your story here your story here your story here your story here your story here your story here your story here your story here your story here</p>
  </article>
  <article class="article col-right" style="top:718px;">
    <h2 class="person-name">BEST MAN’S NAME</h2>
    <div class="photo" role="img" aria-label="Best man photo"><span class="photo-label">His Photo Here</span></div>
    <p class="story"><span class="drop-cap">Y</span>our story here your story here your story here your story here your story here your story your story here your story here your story here your story here your story here your story here your story here your story here your story here your story here</p>
  </article>
  <article class="article col-left" style="top:956px;">
    <h2 class="person-name">BEST MAN’S NAME</h2>
    <div class="photo" role="img" aria-label="Best man photo"><span class="photo-label">His Photo Here</span></div>
    <p class="story"><span class="drop-cap">Y</span>our story here your story here your story here your story here your story here your story your story here your story here your story here your story here your story here your story here your story here your story here your story here your story here</p>
  </article>
  <article class="article col-right" style="top:953px;">
    <h2 class="person-name">BEST MAN’S NAME</h2>
    <div class="photo" role="img" aria-label="Best man photo"><span class="photo-label">His Photo Here</span></div>
    <p class="story"><span class="drop-cap">Y</span>our story here your story here your story here your story here your story here your story your story here your story here your story here your story here your story here your story here your story here your story here your story here your story here</p>
  </article>
</div>
</body>
</html>
```